Fernhold Capital - Web Design

I have recently established a business called Fernhold Capital. The business is focused on providing property developers with project financing solutions. This is not a real estate website so please do not provide such pics or design. I provide financial solutions.

I have been in the financial markets for the past 20 years covering all asset classes from trading through to portfolio management, structuring and business development. The majority of this time was spent with building new business and expanding into new opportunities.

This is a start-up business so there isn't much content at this stage. Therefore, its all about first impressions. I want a design that portray confidence; and that I can deliver a workable solution. It must provide the perception of sophistication, innovation, yet simplistic so its not trying to deceive/hide something. Most importantly it must give the Client a sense of trust and reliability.

I would like to have the website portray my depth of experience in providing financing solutions and consultancy services in achieving the investment objectives. However, I would like to avoid looking like a one man band. I do have access to resources just not directly employed by the company.

Anyway, I hope this is enough to at least wet your appetite. I recently had a logo created on PixelGuild that should set the theme/style of the website

Project Deadline Extended
Reason: Increase time to allow web designer/developer more time to understand the style I am after.

All, Thank you for your current designs. I am based in Singapore, however, I am currently traveling today but will respond by later tonight or tomorrow. Owen

All, A general observation. Please do not include photos of houses, architectural drawings or images that portal construction or real estate. This implies I am either a property agent or in some way directly involve in selling property...very misleading. Remember, I am involved in provide financial solutions not selling property. Owen

All, Please avoid using numerous people within the site as it may represent that my business has a large number of staff when in fact its only me. However, I also don't want to look like a "one man band". So be balanced on using people - I am not sure I want people at all. Thanks Owen

Some designers are not reading the brief or previous messages. If you do more then once I will simply not comment and eliminate ask not to provide any more.

please stop using pictures and/or logos that imply - I manage their money - I protect their money - I grow their money - I offer homes loans - that I do house calls with individuals (i.e no couples shaking heads with a guy) - no house pictures or symbols i.e. it looks like a property website - I have a large organisation (i.e. team of people) If any design include the above I will eliminate it REMEMBER: I am providing innovative financial solutions - NOT asset/fund manager, bank manager or real estate manager thank you

All Please be creative and innovative with your pics. Also ensure you have the rights to use the pics. I have seen basic stock photos being used and again have not read by brief or previous comments. For instance, they use the words "sustainable growth" in google and click on images and you will see most of the images being used. these will be eliminated instantly and not asked to return.

Please, if you use the name of the Company as a Label or Statement can please ensure it remains in the same style as the Logo, i.e. all Caps Large with small.

All, I have decided that I don't want to have people in the main pic on the front page so please provide other inspirational pics. Thanks

guys I found a coffee advert whilst in Vietnam. I like the colour selection and thought it would be inspirational.i ahve added it yo my bried f

Real Estate

Coded - Design and coding required

```html
<!DOCTYPE html>
<html lang="en">
<head>
<meta charset="utf-8">
<title>Fernhold Capital</title>
<link href="https://fonts.googleapis.com/css2?family=Open+Sans:wght@400;600&family=Raleway:wght@300;400;500;600;700&display=swap" rel="stylesheet">
<style>
:root{
  --black:#000;
  --footer:#1f1f1f;
  --gold:#b3a042;
  --gold-text:#a88e1f;
  --gold-light:#c9b04a;
  --gold-dark:#97822a;
  --dark-btn:#3b3413;
  --ink:#222;
  --muted:#6e6e6e;
  --white:#fff;
}
*{margin:0;padding:0;box-sizing:border-box}
html,body{width:797px;height:1200px;overflow:hidden;background:var(--white)}
body{position:relative;font-family:"Open Sans",Arial,sans-serif;color:var(--ink)}
.abs{position:absolute}

.site-header{left:0;top:0;width:797px;height:70px;background:var(--black)}
.brand{left:92px;top:20px;display:flex;align-items:center;gap:9px}
.brand-mark{width:28px;height:28px;background:var(--gold)}
.brand-name{font-family:"Raleway",sans-serif;font-weight:700;font-size:17px;letter-spacing:1.5px;color:var(--gold-light);text-transform:uppercase}
.phone{right:99px;top:30px;text-align:right;color:var(--white)}
.phone-label{font-size:8px;display:block}
.phone-number{font-size:13px;display:flex;align-items:center;gap:4px;margin-top:1px}

.main-nav{left:0;top:70px;width:797px;height:29px;background:linear-gradient(var(--gold-light),var(--gold-dark));display:flex;padding-left:108px}
.main-nav a{font-family:"Raleway",sans-serif;font-weight:600;font-size:9.5px;color:var(--white);text-decoration:none;display:flex;align-items:center;justify-content:center;height:29px;border-right:1px solid rgba(80,65,10,.45)}
.main-nav a:last-child{border-right:none}

.hero{left:0;top:99px;width:797px;height:298px;
  background:
    radial-gradient(ellipse 60% 10% at 55% 88%,rgba(255,205,120,.55),transparent 70%),
    radial-gradient(ellipse 30% 40% at 15% 45%,rgba(120,200,230,.45),transparent 70%),
    radial-gradient(ellipse 25% 45% at 75% 40%,rgba(30,45,70,.55),transparent 70%),
    linear-gradient(180deg,#4f98da 0%,#3f83c4 18%,#35618f 42%,#243a55 62%,#1a2636 78%,#5b5445 87%,#2a3441 92%,#1a2230 100%)}
.hero-caption{left:188px;top:89px;width:412px;height:88px;background:rgba(20,30,45,.6);text-align:center;color:var(--white)}
.hero-title{font-family:"Raleway",sans-serif;font-weight:700;font-size:24px;margin-top:20px}
.hero-sub{font-family:"Raleway",sans-serif;font-weight:500;font-size:12px;margin-top:3px}
.hero-arrow{top:103px}

.service{top:420px;width:150px;text-align:center}
.service-photo{width:100px;height:100px;border-radius:50%;margin:0 auto}
.service h3{font-family:"Raleway",sans-serif;font-weight:500;font-size:11.5px;color:var(--gold-text);margin-top:5px;white-space:nowrap}
.service p{font-size:7px;line-height:11.4px;color:var(--muted);margin:1px auto 0;width:140px}
.btn{display:inline-block;background:var(--ink);color:var(--white);font-family:"Raleway",sans-serif;font-weight:600;font-size:7px;padding:5px 12px;border-radius:2px;margin-top:7px}

.about{left:0;top:638px;width:797px;height:215px;background:var(--gold);text-align:center;color:var(--white)}
.about h2{font-family:"Raleway",sans-serif;font-weight:400;font-size:21px;margin-top:47px}
.about p{font-size:7px;line-height:11.5px;width:600px;margin:8px auto 0}
.about .btn{background:var(--dark-btn);font-size:8px;padding:6px 17px;margin-top:14px}

.col-title{font-family:"Raleway",sans-serif;font-size:15px;font-weight:400}
.projects-title{left:92px;top:880px;color:var(--gold-text)}
.news-title{left:418px;top:880px;color:var(--ink)}
.project{left:92px;display:flex;gap:8px;width:300px}
.thumb{width:100px;height:68px;flex:none}
.item-title{font-size:8.5px;font-weight:400;color:var(--ink)}
.item-text{font-size:6.6px;line-height:11.3px;color:var(--muted);margin-top:2px}
.more{font-size:6.6px;font-weight:600;color:var(--ink);margin-top:2px}
.news-main{left:418px;top:909px;display:flex;gap:9px;width:290px}
.news-line{left:421px;width:290px}

.site-footer{left:0;top:1122px;width:797px;height:78px;background:var(--footer)}
.footer-links{left:96px;top:20px;font-size:9.5px;color:var(--white)}
.footer-links span{margin:0 4px;color:#ccc}
.copyright{left:96px;top:39px;font-size:7px;color:#777}
.social{right:99px;top:23px;display:flex;gap:6px}
.social i{width:13px;height:13px;border-radius:50%;background:var(--gold);display:block}
</style>
</head>
<body>

<header class="site-header abs">
  <div class="brand abs"><span class="brand-mark"></span><span class="brand-name">Fernhold Capital</span></div>
  <div class="phone abs">
    <span class="phone-label">Phone Support</span>
    <span class="phone-number">
      <svg width="11" height="11" viewBox="0 0 24 24"><path fill="#c9b04a" d="M6.6 10.8a15 15 0 0 0 6.6 6.6l2.2-2.2c.3-.3.7-.4 1-.2 1.1.4 2.3.6 3.6.6.6 0 1 .4 1 1V20c0 .6-.4 1-1 1A17 17 0 0 1 3 4c0-.6.4-1 1-1h3.5c.6 0 1 .4 1 1 0 1.3.2 2.5.6 3.6.1.3 0 .7-.2 1z"/></svg>
      02 5550 7312
    </span>
  </div>
</header>

<nav class="main-nav abs">
  <a style="width:56px">HOME</a><a style="width:76px">ABOUT US</a><a style="width:74px">SERVICES</a><a style="width:81px">FINANCING</a><a style="width:75px">PROJECTS</a><a style="width:57px">NEWS</a><a style="width:90px">TESTIMONIAL</a><a style="width:78px">CONTACT</a>
</nav>

<section class="hero abs" role="img" aria-label="City skyline with towers at dusk over the waterfront, lights reflected in the water">
  <div class="hero-caption abs">
    <h1 class="hero-title">PROJECT FINANCING SOLUTIONS</h1>
    <p class="hero-sub">CUM SOCIIS NATOQUE PENATIBUS PARTURIENT</p>
  </div>
  <svg class="hero-arrow abs" style="left:66px" width="14" height="50" viewBox="0 0 14 50"><polyline points="13,1 1,25 13,49" fill="none" stroke="#fff" stroke-width="1.5"/></svg>
  <svg class="hero-arrow abs" style="left:710px" width="14" height="50" viewBox="0 0 14 50"><polyline points="1,1 13,25 1,49" fill="none" stroke="#fff" stroke-width="1.5"/></svg>
</section>

<div class="service abs" style="left:91px">
  <div class="service-photo" role="img" aria-label="Colleagues working together at an office desk" style="background:radial-gradient(circle at 70% 70%,rgba(40,45,60,.7),transparent 45%),radial-gradient(circle at 25% 55%,#3e5f9a,transparent 40%),linear-gradient(135deg,#e9edf2,#b9c3cf 55%,#8a96a6)"></div>
  <h3>Trading Services</h3>
  <p>Aisi eleifend libero a tempus libero lectus feugiat felis Morbi diam mauris viverra in gravida eu mattis in ante</p>
  <span class="btn">READ MORE</span>
</div>
<div class="service abs" style="left:247px">
  <div class="service-photo" role="img" aria-label="Business partners shaking hands" style="background:radial-gradient(circle at 30% 70%,#2f4d8a,transparent 45%),radial-gradient(circle at 72% 45%,#e8dcc8,transparent 40%),linear-gradient(135deg,#dfe6ef,#8fa3c2 50%,#3a4f78)"></div>
  <h3>Business Development</h3>
  <p>Aisi eleifend libero a tempus libero lectus feugiat felis Morbi diam mauris viverra in gravida eu mattis in ante</p>
  <span class="btn">READ MORE</span>
</div>
<div class="service abs" style="left:402px">
  <div class="service-photo" role="img" aria-label="Financial charts and a laptop on a desk" style="background:radial-gradient(circle at 75% 20%,#2c2f35,transparent 30%),radial-gradient(circle at 40% 65%,#7aa0d0,transparent 35%),linear-gradient(160deg,#f4f5f7,#dde2ea 60%,#a9b2bf)"></div>
  <h3>Financial Services</h3>
  <p>Aisi eleifend libero a tempus libero lectus feugiat felis Morbi diam mauris viverra in gravida eu mattis in ante</p>
  <span class="btn">READ MORE</span>
</div>
<div class="service abs" style="left:557px">
  <div class="service-photo" role="img" aria-label="Cupped hands holding a young green plant" style="background:radial-gradient(circle at 50% 42%,#4f8a3a,transparent 14%),radial-gradient(ellipse 60% 35% at 50% 60%,#c9a184,transparent 70%),linear-gradient(160deg,#6f98b8,#2f4456 60%,#141c22)"></div>
  <h3>Management</h3>
  <p>Aisi eleifend libero a tempus libero lectus feugiat felis Morbi diam mauris viverra in gravida eu mattis in ante</p>
  <span class="btn">READ MORE</span>
</div>

<section class="about abs">
  <h2>ABOUT FERNHOLD CAPITAL</h2>
  <p>Vivamus porttitor purus nisi eleifend libero a tempus libero lectus feugiat felis Morbi diam mauris viverra in gravida eu mattis in ante Morbi eget arcu Morbi porta libero id ullamcorper nonummy nibh ligula pulvinar metus eget consectetuer augue nisi quis lacus Ut ac mi quis lacus mollis aliquam Curabitur iaculis tempus eros Curabitur vel mi sit amet magna malesuada ultrices Ut nisi erat fermentum vel congue id euismod in elit Fusce ultricies orci ac feugiat suscipit leo massa sodales velit et</p>
  <p>Morbi ornare gravida elit Integer congue augue et malesuada iaculis ipsum dui aliquet felis at cursus magna nisl nec elit Praesent elementum elit at tellus nec ultricies sit amet porttitor mattis enim In massa libero interdum nec interdum vel blandit sed nulla In ullamcorper est eget tempor cursus neque mi consectetuer mi a ultricies massa</p>
  <span class="btn">READ MORE</span>
</section>

<h2 class="col-title projects-title abs">Recent Projects</h2>
<article class="project abs" style="top:908px">
  <div class="thumb" role="img" aria-label="Silhouettes at an office window at sunset" style="background:radial-gradient(ellipse 45% 40% at 50% 55%,#f3d9a0,transparent 75%),linear-gradient(180deg,#8a8f95 0%,#c9a56c 40%,#8a6a40 70%,#1c1a17 100%)"></div>
  <div>
    <h3 class="item-title">Project Tittle here</h3>
    <p class="item-text">Cum sociis natoque penatibus et magnis dis parturient montes nascetur ridiculus mus In iaculis facilisis massa Etiam eu urna Sed porta Suspendisse quam leo molestie sed luctus quis feugiat in pede Fusce</p>
    <p class="more">READ MORE</p>
  </div>
</article>
<article class="project abs" style="top:995px">
  <div class="thumb" role="img" aria-label="Open hand holding coins with a seedling over grass" style="background:radial-gradient(ellipse 45% 25% at 45% 65%,#d9b49a,transparent 75%),linear-gradient(180deg,#eef5f9 0%,#d7e6ee 45%,#9cc56a 75%,#5e9a2e 100%)"></div>
  <div style="padding-left:3px">
    <h3 class="item-title">Project Tittle here</h3>
    <p class="item-text">Cum sociis natoque penatibus et magnis dis parturient montes nascetur ridiculus mus In iaculis facilisis massa Etiam eu urna Sed porta Suspendisse quam leo molestie sed luctus quis feugiat in pede Fusce</p>
    <p class="more">READ MORE</p>
  </div>
</article>

<h2 class="col-title news-title abs">News &amp; Blog</h2>
<article class="news-main abs">
  <div class="thumb" style="width:102px;height:61px;background:linear-gradient(180deg,#7fb0de 0%,#a9c8e6 30%,#8c96a1 50%,#6c7580 65%,#5d8a45 80%,#3f6a2c 100%)" role="img" aria-label="City towers behind green trees"></div>
  <div style="padding-top:2px">
    <h3 class="item-title" style="font-size:8.8px">Lorem ipsum dolor</h3>
    <p class="item-text">Class aptent taciti sociosqu ad litora torquent per conubia nostra per inceptos hymenaeos Proin nulla arcu nonummy luctus dictum eget ferme</p>
    <p class="item-text" style="color:var(--ink)">Posted on 10 Dec 2014</p>
  </div>
</article>
<article class="news-line abs" style="top:983px">
  <h3 class="item-title">Morbi ornare gravida elit Intege</h3>
  <p class="item-text">Class aptent taciti sociosqu ad litora torquent per conubia nostra per inceptos hymenaeos</p>
</article>
<article class="news-line abs" style="top:1019px">
  <h3 class="item-title">Vivamus porttitor purus</h3>
  <p class="item-text">Class aptent taciti sociosqu ad litora torquent per conubia nostra per inceptos hymenaeos Proin nulla arcu nonummy luctus dictum eget fermentum et lorem Nunc porta</p>
</article>

<footer class="site-footer abs">
  <div class="footer-links abs">About Us<span>|</span>Services<span>|</span>Financing<span>|</span>Projects<span>|</span>News<span>|</span>Testimonials<span>|</span>Contact</div>
  <div class="copyright abs">© 2015 Company Name &nbsp;All right reserved &nbsp;Term of Use</div>
  <div class="social abs"><i></i><i></i><i></i><i></i></div>
</footer>

</body>
</html>
```